Stock Market Research Company Needs a new Design for our Podcast

We need a new logo and social media images for our podcast called Ledger Chat Podcast. We have a current design and logo but are looking to update the branding of the podcast. The podcast is highly interactive taking listener questions each week on individual stocks as well as stock portfolio building strategies.

Copy of Ledger Chat Podcast Thumbnail is our current branding.

Podcast Ad 2 Image attached for an idea of what we're looking for but using our specific colours.

Incorporate K from our current logo (attached)
Colours: Primary Color: (#1AA897), Secondary Color (#2E4151)
Clean/Modern style
Include Headshots of Hosts (images attached)

Target Market(s)

Podcast listeners and stock market investors

Industry/Entity Type

Investment

Logo Text

Title - Ledger Chat Podcast. Tagline - Stock Picks, Strategies & Tips For All Investors

Colors
33b8a4
86cfc6
00a990

Requirements
Must have
• Incorporate K from our current logo (attached)
Clean/Modern style

```html
<!DOCTYPE html>
<html lang="en">
<head>
<meta charset="utf-8">
<title>Ledger Chat Podcast Thumbnail</title>
<link rel="stylesheet" href="https://fonts.googleapis.com/css2?family=Oswald:wght@700&family=Roboto+Slab:wght@400;700&family=Raleway:wght@500&display=swap">
<style>
  :root {
    --teal: #22ab97;
    --navy-deep: #17273a;
    --navy: #1f3550;
    --white: #ffffff;
    --page: #ffffff;
  }
  html, body { margin: 0; padding: 0; overflow: hidden; }
  body { width: 1200px; height: 1200px; background: var(--page); position: relative; }
  .thumbnail {
    position: absolute; left: 0; top: 240px; width: 1200px; height: 720px;
    overflow: hidden;
    background: linear-gradient(100deg, var(--navy-deep) 0%, #1a2d44 55%, #22395a 100%);
  }
  .backdrop-scene {
    position: absolute; right: 0; top: 0; width: 620px; height: 720px;
    background: radial-gradient(ellipse at 65% 35%, rgba(70,100,135,0.45), rgba(23,39,58,0) 70%);
  }
  .grid-lines { position: absolute; inset: 0; }
  .title {
    position: absolute; left: 81px; top: 84px; margin: 0; z-index: 2;
    width: 590px; overflow: hidden;
    font-family: "Oswald", sans-serif; font-weight: 700; font-size: 104px;
    line-height: 1; letter-spacing: 0; white-space: nowrap;
  }
  .title .accent { color: var(--teal); }
  .title .main { color: var(--white); }
  .badge {
    position: absolute; left: 687px; top: 93px; width: 429px; height: 106px; z-index: 2;
    background: var(--teal); color: var(--white);
    display: flex; align-items: center; justify-content: center;
    font-family: "Roboto Slab", serif; font-weight: 700; font-size: 68px; letter-spacing: 1px;
    white-space: nowrap;
  }
  .tagline {
    position: absolute; left: 81px; top: 258px; margin: 0; z-index: 2;
    font-family: "Roboto Slab", serif; font-weight: 400; font-size: 50px;
    line-height: 72px; color: var(--white); text-transform: uppercase; white-space: nowrap;
  }
  .brand { position: absolute; left: 81px; top: 500px; width: 434px; text-align: center; z-index: 3; }
  .brand-square { width: 64px; height: 64px; background: var(--teal); margin: 0 auto 22px; }
  .brand-name {
    font-family: "Raleway", sans-serif; font-weight: 500; font-size: 34px;
    color: var(--teal); letter-spacing: 0.5px; line-height: 1; white-space: nowrap;
  }
  .brand-tagline {
    margin-top: 16px; font-family: "Raleway", sans-serif; font-weight: 500;
    font-size: 18px; letter-spacing: 3px; color: var(--white); white-space: nowrap;
  }
  .host {
    position: absolute; bottom: 0; border-radius: 150px 150px 0 0; z-index: 1;
    background: linear-gradient(180deg, #3a4350 0%, #2a313b 55%, #1e242c 100%);
  }
  .host-one { left: 540px; width: 370px; height: 384px; }
  .host-two { left: 860px; width: 340px; height: 388px; background: linear-gradient(180deg, #55606b 0%, #414a54 55%, #30363e 100%); }
</style>
</head>
<body>
  <section class="thumbnail">
    <div class="backdrop-scene" role="img" aria-label="Faded photo of a businessman pointing at financial charts"></div>
    <svg class="grid-lines" width="1200" height="720" viewBox="0 0 1200 720" aria-hidden="true">
      <g stroke="rgba(255,255,255,0.05)" stroke-width="40" fill="none">
        <path d="M0 200 L180 0"/>
        <path d="M60 720 L410 300 L760 720"/>
        <path d="M300 0 L560 300"/>
      </g>
    </svg>
    <h1 class="title"><span class="accent">LEDGER</span> <span class="main">CHAT</span></h1>
    <div class="badge">PODCAST</div>
    <p class="tagline">Stock Picks,<br>Strategies &amp; Tip<br>For Investors</p>
    <div class="host host-one" role="img" aria-label="Headshot of the first podcast host in a dark suit"></div>
    <div class="host host-two" role="img" aria-label="Headshot of the second podcast host in a grey suit"></div>
    <div class="brand">
      <div class="brand-square"></div>
      <div class="brand-name">NORTHGATE FINANCIAL</div>
      <div class="brand-tagline">INDEPENDENT EQUITY ADVISORS</div>
    </div>
  </section>
</body>
</html>
```